Business Card Upgrade

I have designed our business card using our new logo. I think it needs imporovements. We used to have two cards for our business. One card was for our software business, and the other was for our consulting business. We are now in the process of combining our websites, marketing, name, and a new logo.

Our goal is to have a really sharp professional logo. One reason I designed the card the way I did was that our Titles are sometimes long, and by separating the person's name and title, it shows up very well and the title can be adjusted no matter how long it is. Sometimes the title can be 4 or 5 words or more.

We really like our logo on black as it shows up very nice. Our PMS colors are as follows: 368C and 459C.

The Designer that will be working with us will need to deliver the following:

The front and back of the Business Card Design will need to be delivered in a high quality JPEG, and
The front and back of the Business Card Design in Illustrator Format .ai
Any fonts will need to be sent to us if they are not standard and are required to open the Illustrator file correctly.

To help us get a good idea of the card with a title, please use the title: " Director of Software Development "

NOTE: The chosen designer will be selected to design our new letterhead within 2 weeks from the closing of this contest.

To help us make sure the card design works with longer titles, please use the followign job title on the card:  

"Director of Software and Product Development"

 

ALL DESIGNERS:

1. I appreciate the different angles you are showing the cards, but please be sure and always show the direct view, so I can see the layout and what the person I hand the card will see.

2. Please do not use white.  Please use off white as I don't care for white cards and they get dirty easy and do not represent the designs well.

Dear Designers,

Please provide samples straight one as a viewer of the card will see.  Some of the angles that are presented make it impossible to tell how everything fits, and sometimes even makes areas look skewed. So, please provide a straight sample view.

Pinnacle 400 company executives such as Vice Presidents, and Directors

Software

• Professional looking Card.

Our customers are Directors, Vice Presidents, and Presidents of companies as large as Pinnacle 400 companies. The card needs to get attention wile still looking professional.

Delivery of the finished product in Illustrator Format with any fonts needed to edit the text or open the file.

The card will be a heavy stock with a soft touch coating for that silk feel.

```html
<!DOCTYPE html>
<html lang="en">
<head>
<meta charset="utf-8">
<title>Harborline Trade Group — Business Card</title>
<link rel="stylesheet" href="https://fonts.googleapis.com/css2?family=Open+Sans:wght@400;600;700&display=swap">
<style>
  :root {
    --backdrop: #b8a898;
    --card: #2b2b2b;
    --brand-green: #6fae2c;
    --text-sand: #d8cb9c;
    --shadow: rgba(0, 0, 0, 0.35);
  }
  * { margin: 0; padding: 0; box-sizing: border-box; }
  html, body {
    width: 1200px;
    height: 900px;
    overflow: hidden;
  }
  body {
    position: relative;
    background: var(--backdrop);
    font-family: "Open Sans", Arial, sans-serif;
  }
  .card {
    position: absolute;
    left: 353px;
    width: 489px;
    height: 278px;
    background: var(--card);
    box-shadow: 0 2px 6px var(--shadow);
  }
  .card--front { top: 154px; }
  .card--back { top: 464px; }

  .wordmark {
    position: absolute;
    color: var(--brand-green);
    font-weight: 700;
    font-size: 30px;
    letter-spacing: 3px;
    line-height: 1;
  }
  .card--front .wordmark { left: 25px; top: 40px; }
  .card--back .wordmark { right: 22px; top: 175px; }

  .holder-name {
    position: absolute;
    left: 26px;
    top: 134px;
    color: var(--text-sand);
    font-weight: 600;
    font-size: 17px;
  }
  .holder-title {
    position: absolute;
    left: 27px;
    top: 160px;
    color: var(--text-sand);
    font-size: 9.5px;
    letter-spacing: 0.3px;
    text-transform: uppercase;
  }
  .contact-list {
    position: absolute;
    left: 24px;
    top: 188px;
    list-style: none;
  }
  .contact-item {
    display: flex;
    align-items: center;
    height: 20px;
    color: var(--text-sand);
    font-size: 11.5px;
  }
  .contact-icon {
    width: 14px;
    height: 12px;
    margin-right: 11px;
    fill: none;
    stroke: var(--brand-green);
    stroke-width: 1.4;
  }
  .rule {
    position: absolute;
    height: 2px;
    background: var(--brand-green);
  }
  .card--front .rule { left: 25px; right: 0; top: 253px; }
  .card--back .rule { left: 0; width: 347px; top: 253px; }

  .website {
    position: absolute;
    right: 22px;
    top: 245px;
    color: var(--text-sand);
    font-size: 12px;
    line-height: 16px;
    letter-spacing: 0.8px;
  }
</style>
</head>
<body>
  <section class="card card--front" aria-label="Business card front">
    <div class="wordmark">HARBORLINE</div>
    <h1 class="holder-name">Dana Whitfield</h1>
    <p class="holder-title">Director of Software and Product Development</p>
    <ul class="contact-list">
      <li class="contact-item">
        <svg class="contact-icon" viewBox="0 0 14 12" aria-hidden="true"><rect x="4" y="0.8" width="6" height="10.4" rx="1"/><line x1="6" y1="9.2" x2="8" y2="9.2"/></svg>
        555.014.2290
      </li>
      <li class="contact-item">
        <svg class="contact-icon" viewBox="0 0 14 12" aria-hidden="true"><rect x="1" y="2" width="12" height="8" fill="var(--brand-green)" stroke="none"/><polyline points="1,2 7,7 13,2" stroke="var(--card)"/></svg>
        dwhitfield@hltrade.com
      </li>
      <li class="contact-item">
        <svg class="contact-icon" viewBox="0 0 14 12" aria-hidden="true"><polyline points="1,6.5 7,1 13,6.5"/><polyline points="3,5 3,11 11,11 11,5"/></svg>
        418 Bayside Avenue, Portview, AL 36000
      </li>
    </ul>
    <div class="rule"></div>
  </section>

  <section class="card card--back" aria-label="Business card back">
    <div class="wordmark">HARBORLINE</div>
    <div class="rule"></div>
    <p class="website">www.hltrade.com</p>
  </section>
</body>
</html>
```